Hvac and insulation company needs good looking business card design

We are hvac and insulation company and looking for a new business cards that look to today standards designs

Target Market(s)

homeowners

Industry/Entity Type

Hvac

Contact Information for Business Card

Name: Dorian Velkova
Home comfort consultant
address: 4827 Marrow Ridge Rd #215 Oakland, CA 94611
office: 888-317-5069
cell: 510-642-1388
Lic.# 458127
Email: dorian@quarry-hvac.com
Web: quarry-hvac.com

Requirements
Must have
• clean and sleek look
Nice to have
• simple with a clean look
Should not have
• to busy business card

```html
<!DOCTYPE html>
<html lang="en">
<head>
<meta charset="utf-8">
<title>Quarry Home Solutions – Business Card</title>
<link href="https://fonts.googleapis.com/css2?family=Open+Sans:wght@400;600;700&display=swap" rel="stylesheet">
<style>
  :root {
    --orange: #ff6a00;
    --charcoal: #333333;
    --band: #4a4a4a;
    --soft-orange: #ffa25c;
    --text-light: #f2f2f2;
    --text-muted: #a8a8a8;
    --backdrop: #ece9e6;
  }
  * { margin: 0; padding: 0; box-sizing: border-box; }
  html, body { width: 1200px; height: 800px; overflow: hidden; }
  body {
    background: var(--backdrop);
    font-family: "Open Sans", Arial, sans-serif;
    display: flex;
    align-items: center;
    justify-content: center;
    gap: 48px;
  }
  .card {
    position: relative;
    width: 540px;
    height: 309px;
    overflow: hidden;
    box-shadow: 0 6px 18px rgba(0,0,0,0.18);
  }

  /* Front */
  .card--front { background: var(--orange); }
  .front-brand {
    position: absolute;
    left: 110px;
    top: 104px;
    display: flex;
    align-items: center;
    gap: 16px;
  }
  .brand-dot {
    width: 58px; height: 58px;
    border-radius: 50%;
    background: var(--charcoal);
  }
  .brand-name {
    font-weight: 700;
    font-size: 64px;
    line-height: 1;
    color: var(--charcoal);
    letter-spacing: 1px;
  }
  .front-tagline {
    position: absolute;
    left: 190px;
    top: 178px;
    font-size: 15px;
    letter-spacing: 5px;
    color: var(--soft-orange);
  }

  /* Back */
  .card--back { background: var(--charcoal); }
  .back-brand {
    position: absolute;
    right: 36px;
    top: 28px;
    display: flex;
    align-items: center;
    gap: 10px;
  }
  .back-brand .brand-dot { width: 30px; height: 30px; background: var(--orange); }
  .back-brand .brand-name { font-size: 34px; color: var(--orange); }
  .back-tagline {
    position: absolute;
    right: 36px;
    top: 68px;
    width: 150px;
    font-size: 9px;
    letter-spacing: 2.5px;
    color: var(--text-muted);
    text-align: right;
  }
  .person {
    position: absolute;
    left: 40px;
    top: 96px;
  }
  .person-name {
    font-weight: 600;
    font-size: 22px;
    color: var(--orange);
    letter-spacing: 0.5px;
  }
  .person-title {
    font-size: 12px;
    letter-spacing: 1.5px;
    color: var(--text-muted);
    margin-top: 1px;
  }
  .contact-list {
    list-style: none;
    margin-top: 8px;
  }
  .contact-list li {
    display: flex;
    align-items: center;
    gap: 10px;
    font-size: 13px;
    color: var(--text-light);
    height: 20px;
  }
  .contact-list svg { width: 13px; height: 13px; fill: var(--orange); flex: none; }
  .address {
    position: absolute;
    left: 30px;
    top: 238px;
    font-size: 13px;
    color: var(--text-light);
  }
  .footer-shape { position: absolute; left: 0; top: 0; }
  .license {
    position: absolute;
    right: 40px;
    top: 234px;
    font-size: 10px;
    color: var(--text-light);
  }
  .website {
    position: absolute;
    right: 40px;
    top: 268px;
    font-size: 16px;
    color: var(--text-light);
    letter-spacing: 0.3px;
  }
</style>
</head>
<body>

  <section class="card card--front">
    <div class="front-brand">
      <span class="brand-dot"></span>
      <span class="brand-name">quarry</span>
    </div>
    <div class="front-tagline">home solutions</div>
  </section>

  <section class="card card--back">
    <svg class="footer-shape" width="540" height="309" viewBox="0 0 540 309">
      <path d="M205 309 L220 270 C226 258 236 254 250 254 L540 254 L540 309 Z" fill="var(--band)"/>
      <path d="M0 262 L180 262 C205 262 212 250 232 250 L540 250" stroke="var(--orange)" stroke-width="1.6" fill="none"/>
    </svg>

    <div class="back-brand">
      <span class="brand-dot"></span>
      <span class="brand-name">quarry</span>
    </div>
    <div class="back-tagline">home solutions</div>

    <div class="person">
      <div class="person-name">Dorian Velkova</div>
      <div class="person-title">Home comfort consultant</div>
      <ul class="contact-list">
        <li>
          <svg viewBox="0 0 24 24" aria-hidden="true"><path d="M6.6 10.8a15.1 15.1 0 0 0 6.6 6.6l2.2-2.2a1 1 0 0 1 1-.25 11.4 11.4 0 0 0 3.6.57 1 1 0 0 1 1 1V20a1 1 0 0 1-1 1A17 17 0 0 1 3 4a1 1 0 0 1 1-1h3.5a1 1 0 0 1 1 1c0 1.25.2 2.45.57 3.57a1 1 0 0 1-.25 1z"/></svg>
          888-317-5069
        </li>
        <li>
          <svg viewBox="0 0 24 24" aria-hidden="true"><path d="M7 1h10a2 2 0 0 1 2 2v18a2 2 0 0 1-2 2H7a2 2 0 0 1-2-2V3a2 2 0 0 1 2-2zm0 3v14h10V4zm5 15.5a1 1 0 1 0 0 2 1 1 0 0 0 0-2z"/></svg>
          510-642-1388
        </li>
        <li>
          <svg viewBox="0 0 24 24" aria-hidden="true"><path d="M2 5h20v14H2zm2 2v.4l8 5.2 8-5.2V7zm0 2.8V17h16V9.8l-8 5.2z"/></svg>
          dorian@quarry-hvac.com
        </li>
      </ul>
    </div>

    <div class="address">4827 Marrow Ridge Rd #215 Oakland, CA 94611</div>
    <div class="license">Lic.# 458127</div>
    <div class="website">www.quarry-hvac.com</div>
  </section>

</body>
</html>
```